Yoga class opening. Little schedule for JUNE JULY and AUGUST

Flyer to promote an opening yoga class. The color of the docx haven't to be respected.

We want something joyfull, professional, clean and serious.

About the logo we oppened a contest at the same time so at the moment there is no logo but the logo color will be simple.

The phone number will change so you can poste a random one for the design that i can change by myself.

i recieved many creation in both side BUT i want something in 1 side :)

Target Market(s)

Yoga student. all age

Industry/Entity Type

It Professional

Logo Text

Yoga fern

Font styles to use
Sans Serif

Requirements
Must have
• The text present on the docx
Nice to have
• Some symbols about yoga ( Namasté signs, mandala, ... )
Should not have
• Not too much details it has to be clear.

```html
<!DOCTYPE html>
<html lang="fr">
<head>
<meta charset="utf-8">
<title>Yoga Fern – Stages d'été</title>
<link href="https://fonts.googleapis.com/css2?family=Roboto:wght@300;400;500&family=Oswald:wght@500&display=swap" rel="stylesheet">
<style>
  :root {
    --plum: #a2509d;
    --plum-dark: #93418f;
    --plum-light: #bd7db8;
    --heading: #9a3d92;
    --grey: #8c8c8c;
    --grey-dark: #7a7a7a;
    --paper: #ffffff;
    --photo-a: #c9dcd8;
    --photo-b: #e27aa9;
  }
  * { margin: 0; padding: 0; box-sizing: border-box; }
  html, body { width: 894px; height: 1200px; overflow: hidden; background: var(--paper); }
  .flyer { position: relative; width: 894px; height: 1200px; font-family: "Roboto", sans-serif; color: var(--grey); }
  .top-wave, .bottom-band { position: absolute; left: 0; }
  .top-wave { top: 0; }
  .bottom-band { top: 1050px; }
  .brand-title { position: absolute; top: 232px; width: 100%; text-align: center; font-size: 42px; font-weight: 500; color: var(--heading); letter-spacing: .5px; }
  .intro { position: absolute; top: 292px; width: 100%; text-align: center; font-size: 21px; font-weight: 400; line-height: 26px; color: var(--grey-dark); text-transform: uppercase; }
  .banner { position: absolute; left: 55px; top: 402px; width: 777px; height: 70px; background: var(--plum); color: #fff; font-size: 17px; font-weight: 300; text-align: center; display: flex; align-items: center; justify-content: center; line-height: 22px; padding: 0 40px; }
  .divider { position: absolute; left: 441px; top: 494px; width: 3px; height: 456px; background: var(--plum); }
  .divider::before { content: ""; position: absolute; left: -12px; top: -12px; width: 27px; height: 27px; border-radius: 50%; background: var(--plum); }
  .column { position: absolute; top: 532px; width: 406px; }
  .column.left { left: 14px; }
  .column.right { left: 468px; }
  .session { margin-bottom: 20px; }
  .session h2 { font-size: 17px; font-weight: 500; color: var(--heading); line-height: 20px; margin-bottom: 2px; }
  .session p { font-size: 14px; font-weight: 300; line-height: 20.5px; }
  .column.right .session p { text-align: justify; }
  .annual-start { position: absolute; left: 305px; top: 975px; width: 278px; height: 43px; background: var(--plum); color: #fff; font-size: 13px; font-weight: 300; text-align: center; line-height: 15px; display: flex; align-items: center; justify-content: center; }
  .brand-mark { position: absolute; left: 722px; top: 960px; width: 156px; text-align: center; }
  .brand-mark .dot { display: block; margin: 0 auto 8px; width: 62px; height: 62px; border-radius: 50%; background: var(--plum-light); }
  .brand-mark .name { font-size: 22px; font-weight: 500; color: var(--plum-dark); text-transform: uppercase; }
  .contact-title { position: absolute; top: 1094px; width: 100%; text-align: center; font-family: "Oswald", sans-serif; font-size: 26px; font-weight: 500; color: #fff; text-transform: uppercase; }
  .contact-list { position: absolute; top: 1150px; width: 100%; display: flex; justify-content: center; gap: 22px; list-style: none; color: #fff; font-size: 20px; font-weight: 300; }
  .contact-list li { display: flex; align-items: center; gap: 10px; }
  .contact-icon { width: 34px; height: 34px; border-radius: 50%; background: #fff; display: flex; align-items: center; justify-content: center; }
</style>
</head>
<body>
<div class="flyer">
  <svg class="top-wave" width="894" height="240" viewBox="0 0 894 240">
    <defs>
      <linearGradient id="photoTone" x1="0" y1="0" x2="1" y2="0">
        <stop offset="0" stop-color="var(--photo-a)"/>
        <stop offset=".7" stop-color="var(--photo-b)"/>
        <stop offset="1" stop-color="var(--photo-a)"/>
      </linearGradient>
    </defs>
    <path role="img" aria-label="Photo d'une femme en tenue rose pratiquant le yoga dans un studio lumineux" d="M210 0 L894 0 L894 140 C760 200 560 205 430 165 C330 130 270 70 210 0 Z" fill="url(#photoTone)"/>
    <path d="M0 0 L210 0 C270 70 330 130 430 165 C560 205 760 200 894 140 L894 160 C760 222 560 228 420 188 C270 145 120 70 0 10 Z" fill="var(--plum-light)"/>
    <path d="M0 10 C120 70 270 145 420 188 C560 228 760 222 894 160 L894 182 C760 242 540 248 400 208 C250 165 100 90 0 36 Z" fill="var(--plum)"/>
  </svg>

  <h1 class="brand-title">YOGA FERN</h1>
  <p class="intro">Nouveau !! Votre studio de yoga a Ixelles<br>Ouverture le 6 juin 2016 au<br>212 Rue des Tilleuls<br>1050 Ixelles</p>

  <div class="banner">EN ATTENDANT LE PLANNING DES COURS DE LA RENTRÉE, YOGA FERN VOUS PROPOSE SES STAGES ET ATELIERS D'ÉTÉ.</div>

  <div class="divider"></div>

  <section class="column left">
    <div class="session">
      <h2>Stage Découverte Du Yoga 10h00 85 € :</h2>
      <p>Du lundi 6 au vendredi 10 juin : 10h00 à 12h00 ou 18h00 à 20h00</p>
      <p>Du lundi 13 au vendredi 17 juin : 10h00 à 12h00 ou 18h00 à 20h00</p>
      <p>Du lundi 20 au vendredi 24 juin : 10h00 à 12h00 ou 18h00 à 20h00</p>
      <p>Du lundi 27 au vendredi 1er juillet : 10h00 à 12h00 ou 18h00 à 20h00</p>
    </div>
    <div class="session">
      <h2>Atelier gestion du Stress Yoga/sophrologie 2h00 28 €:</h2>
      <p>Samedi 11 Juin 10h30 À 12h30<br>Samedi 11 Juin 15h À 17h00<br>Dimanche 12 Juin 10h30 À 12h30<br>Dimanche 12 Juin 14h À 16h00</p>
    </div>
    <div class="session">
      <h2>Atelier Gestion Du Stress Yoga/sophrologie 2h00 28 €:</h2>
      <p>Samedi 9 Juillet 10h30 À 12h30<br>Samedi 9 Juillet 15h00 À 17h00<br>Dimanche 10 Juillet 10h30 À 12h30<br>Dimanche 10 Juillet 14h00 À 16h00</p>
    </div>
  </section>

  <section class="column right">
    <div class="session">
      <h2>Stage Initiation À L'ashtanga 10h00 85 €:</h2>
      <p>Du Lundi 4 Au Vendredi 8 Juillet : 10h00 À 12h00 Ou 18h00 À 20h00</p>
      <p>Du Lundi 11 Au Vendredi 15 Juillet : 10h00 À 12h00 Ou 18h00 À 20h00</p>
      <p>Du Lundi 18 Au Vendredi 22 Juillet : 10h00 À 12h00 Ou 18h00 À 20h00</p>
      <p>Du Lundi 25 Au Vendredi 29 Juillet : 10h00 À 12h00 Ou 18h00 À 20h00</p>
    </div>
    <div class="session">
      <h2>Stage Découverte Du Yoga 10h00 85 €:</h2>
      <p>Du lundi 1er au vendredi 5 août : 10h00 à 12h00 ou 18h00 à 20h00</p>
      <p>Du lundi 8 au vendredi 12 août: 10h00 à 12h00 ou 18h00 à 20h00</p>
      <p>Du lundi 15 au vendredi 19 août: 10h00 à 12h00 ou 18h00 à 20h00</p>
      <p>Du lundi 22 au vendredi 26 août: 10h00 à 12h00 ou 18h00 à 20h00</p>
    </div>
  </section>

  <div class="annual-start">DÉMARRAGE DU PLANNING ANNUEL LE<br>5 SEPTEMBRE 2016</div>

  <div class="brand-mark">
    <span class="dot"></span>
    <span class="name">Yoga Fern</span>
  </div>

  <svg class="bottom-band" width="894" height="150" viewBox="0 0 894 150">
    <path d="M0 38 Q447 -20 894 38 L894 150 L0 150 Z" fill="var(--plum)"/>
  </svg>

  <h2 class="contact-title">Contact us</h2>
  <ul class="contact-list">
    <li>
      <span class="contact-icon">
        <svg width="20" height="20" viewBox="0 0 24 24"><path d="M6.6 10.8a15.2 15.2 0 0 0 6.6 6.6l2.2-2.2a1 1 0 0 1 1-.25 11.4 11.4 0 0 0 3.6.57 1 1 0 0 1 1 1V20a1 1 0 0 1-1 1A17 17 0 0 1 3 4a1 1 0 0 1 1-1h3.5a1 1 0 0 1 1 1c0 1.25.2 2.45.57 3.57a1 1 0 0 1-.25 1z" fill="var(--plum)"/></svg>
      </span>
      (123) 555 0148 2260
    </li>
    <li><span class="contact-icon"></span>yoga fern</li>
    <li><span class="contact-icon"></span>yogafern@social</li>
  </ul>
</div>
</body>
</html>
```